LUNE clinical trial results infographic

We need an infographic which presents the results from the LUNE research trial. It should be colourful and engaging, in understandable language and showing the steps to get to the results. This is to showcase the results to patients/the public/clinicians, giving a brief summary of what the study proved. The final design should have the LUNE logo at the top (please see the logo on the attached Word document)
I have attached the required logos which need to be used (LUNE - within the Word doc, Kestrel Injury and Acute Care, Marlow Vale University, PTQ - see also their design pack attached) as well as an example from another study, VELKOR3, as an example of what the layout could look like. Please DO NOT use the content from the VELKOR3 example though, please instead use the content from the attached document 'InfographicDesignInformation_LUNE_PixelBazaar_02Dec2025'. Please also include information about the funding in a footer at the bottom of the infographic (as per the above document).

```html
<!DOCTYPE html>
<html lang="en">
<head>
<meta charset="utf-8">
<title>LUNE trial results infographic</title>
<link rel="stylesheet" href="https://fonts.googleapis.com/css2?family=Poppins:wght@400;500;600;700;800&family=Oswald:wght@500;600&display=swap">
<style>
  :root {
    --navy: #0d2a6b;
    --blue: #0f4a8f;
    --bright-blue: #1b55a8;
    --grey-pill: #8c8c8c;
    --pale-blue: #cddff8;
    --orange: #f07d1a;
    --ink: #1b1b1b;
    --page-bg: #e6e6e6;
    --white: #ffffff;
  }
  * { box-sizing: border-box; margin: 0; padding: 0; }
  html, body { width: 1200px; height: 1200px; overflow: hidden; background: var(--page-bg); }
  body { position: relative; font-family: "Poppins", sans-serif; color: var(--ink); }

  .poster {
    position: absolute; left: 189px; top: 20px;
    width: 1242px; height: 1755px;
    background: var(--white);
    transform: scale(0.661); transform-origin: top left;
    overflow: hidden;
  }
  .abs { position: absolute; }

  .study-mark { left: 74px; top: 66px; display: flex; align-items: center; gap: 16px; }
  .study-mark .mark-square { width: 34px; height: 34px; background: var(--blue); }
  .study-mark .mark-name { font-family: "Poppins", sans-serif; font-weight: 800; font-size: 92px; line-height: 1; color: var(--blue); letter-spacing: 2px; }

  .university-tab {
    left: 954px; top: 52px; width: 288px; height: 138px;
    background: var(--navy); border-radius: 70px 0 0 70px;
    display: flex; flex-direction: column; align-items: center; justify-content: center; gap: 10px;
    padding-left: 30px;
  }
  .university-tab .uni-circle { width: 44px; height: 44px; border-radius: 50%; border: 2px solid var(--white); }
  .university-tab .uni-name { color: var(--white); font-weight: 500; font-size: 17px; letter-spacing: 1px; text-align: center; line-height: 1.2; }

  .headline { left: 0; width: 1242px; text-align: center; top: 206px; }
  .headline .line-one { font-weight: 600; font-size: 41px; color: var(--ink); line-height: 1.1; }
  .headline .line-two { font-weight: 800; font-size: 53px; color: var(--bright-blue); line-height: 1.15; }

  .background-band { left: 0; top: 343px; width: 1242px; height: 332px; background: var(--blue); }
  .band-visual {
    left: 830px; top: 343px; width: 412px; height: 332px;
    background: linear-gradient(135deg, #1f3f7a 0%, #f3c2a4 55%, #a8a8a8 100%);
  }
  .band-tab { left: 355px; top: 324px; width: 530px; height: 64px; }
  .band-tab-label { left: 355px; top: 334px; width: 530px; text-align: center; color: var(--white); font-weight: 700; font-size: 30px; }
  .band-copy { left: 73px; top: 410px; width: 768px; color: var(--white); font-size: 16px; line-height: 1.25; text-align: justify; }
  .band-copy p + p { margin-top: 20px; }

  .section-pill {
    background: var(--grey-pill); color: var(--white); border-radius: 12px;
    font-weight: 700; font-size: 28px; text-align: center; line-height: 42px; height: 42px;
  }
  .section-pill small { font-size: 14px; font-weight: 600; }

  .placeholder-art { border-radius: 6px; }
  .gym-art { left: 70px; top: 750px; width: 150px; height: 150px; border-radius: 50%; background: linear-gradient(160deg, #dfe7f4 0%, #1b3a6e 100%); }
  .scale-art { left: 352px; top: 748px; width: 140px; height: 180px; background: linear-gradient(160deg, #3a3a3a 0%, #d32424 100%); }
  .key-caption { font-size: 17px; line-height: 1.2; color: var(--ink); }
  .key-caption b { font-weight: 700; }

  .findings-box { left: 604px; top: 755px; width: 576px; height: 165px; background: var(--pale-blue); border-radius: 8px; padding: 22px 30px 0 34px; }
  .tick-list { list-style: none; }
  .tick-list li { position: relative; padding-left: 22px; }
  .tick-list li::before {
    content: ""; position: absolute; left: 0; top: 0.42em; width: 12px; height: 12px; border-radius: 50%;
    background: var(--orange);
  }
  .tick-list li::after {
    content: ""; position: absolute; left: 3.5px; top: calc(0.42em + 2.5px); width: 3px; height: 5px;
    border: solid var(--white); border-width: 0 1.6px 1.6px 0; transform: rotate(45deg);
  }
  .findings-box .tick-list li { font-size: 19px; line-height: 1.17; color: var(--ink); }
  .findings-box .tick-list li + li { margin-top: 14px; }

  .dashed-rule { left: 62px; width: 1118px; border-top: 2px dashed #9a9a9a; }

  .patient-art { left: 80px; top: 1030px; width: 185px; height: 220px; background: linear-gradient(180deg, #e8eef7 0%, #2a4a86 100%); }
  .age-pill { left: 85px; top: 1254px; width: 180px; height: 22px; background: var(--grey-pill); border-radius: 8px; color: var(--white); font-size: 16px; text-align: center; line-height: 22px; }
  .age-pill b { font-weight: 700; }
  .foot-art { left: 620px; top: 1072px; width: 200px; height: 205px; background: linear-gradient(150deg, #1b55a8 0%, #f2d6c6 50%, #e4a14a 100%); }

  .criteria-heading { font-family: "Oswald", sans-serif; font-weight: 600; font-size: 30px; color: var(--bright-blue); line-height: 1; }
  .criteria-list li { font-size: 16px; line-height: 1.05; color: var(--ink); }
  .criteria-list li + li { margin-top: 16px; }

  .detail-col { top: 1385px; height: 175px; text-align: center; display: flex; flex-direction: column; align-items: center; justify-content: center; }
  .detail-divider { top: 1382px; width: 14px; height: 180px; background: linear-gradient(90deg, rgba(0,0,0,0.12), rgba(0,0,0,0)); }
  .detail-icon { width: 62px; height: 62px; border-radius: 10px; margin-bottom: 10px; }
  .detail-big { font-family: "Oswald", sans-serif; font-weight: 600; color: var(--bright-blue); font-size: 30px; line-height: 1.05; }
  .detail-small { font-size: 16px; line-height: 1.2; color: var(--ink); }
  .detail-accent { font-family: "Oswald", sans-serif; font-weight: 500; color: var(--bright-blue); font-size: 17px; margin-top: 6px; }

  .contact-email { left: 60px; top: 1640px; display: flex; align-items: center; gap: 10px; font-weight: 500; font-size: 24px; color: var(--ink); }
  .partner-row { left: 60px; top: 1684px; display: flex; align-items: center; gap: 18px; }
  .partner { display: flex; align-items: center; gap: 6px; font-size: 14px; color: #555; font-weight: 400; }
  .partner .partner-square { width: 20px; height: 20px; }
  .funder-copy { left: 695px; top: 1637px; width: 490px; font-size: 16px; line-height: 1.25; color: var(--ink); }
  .footer-bar { left: 0; top: 1738px; width: 1242px; height: 17px; background: var(--navy); }
</style>
</head>
<body>
<main class="poster">

  <div class="abs study-mark">
    <span class="mark-square"></span>
    <span class="mark-name">LUNE</span>
  </div>

  <div class="abs university-tab">
    <span class="uni-circle"></span>
    <span class="uni-name">MARLOW VALE<br>UNIVERSITY</span>
  </div>

  <h1 class="abs headline">
    <span class="line-one" style="display:block">PATIENTS CAN SAFELY START WALKING SOON</span>
    <span class="line-two" style="display:block">AFTER SURGERY ON A BROKEN ANKLE</span>
  </h1>

  <div class="abs background-band"></div>
  <div class="abs band-visual" role="img" aria-label="Illustration of a foot and ankle skeleton with a highlighted injury point"></div>
  <svg class="abs band-tab" viewBox="0 0 530 64" aria-hidden="true">
    <path d="M0 19 Q10 0 40 2 L490 2 Q520 0 530 19 L530 19 Z" fill="#3c3c3c"/>
    <path d="M30 19 L500 19 L462 56 Q456 64 440 64 L90 64 Q74 64 68 56 Z" fill="#8c8c8c"/>
  </svg>
  <h2 class="abs band-tab-label">BACKGROUND</h2>
  <div class="abs band-copy">
    <p>Ankle fractures are very common, and often require an operation. After surgery for ankle fracture, patients are usually advised to avoid walking for 6 weeks (delayed weight-bearing). An alternative is to walk 2 weeks after surgery (early weight-bearing).</p>
    <p>In this study, half of the patients were instructed that they should put as much weight through their affected leg as they felt comfortable and without causing pain. The other half were instructed to avoid putting any weight through their operated leg for six weeks after surgery.</p>
    <p>After 4 months, ankle function was similar, and the number of complications was similar, in the two groups. The cost to the PHS and social services were also similar, with slightly lower costs in the early weight-bearing group.</p>
  </div>

  <h2 class="abs section-pill" style="left:400px; top:695px; width:440px;">KEY MESSAGES/FINDINGS</h2>
  <div class="abs placeholder-art gym-art" role="img" aria-label="Illustration of a patient exercising in a gym"></div>
  <p class="abs key-caption" style="left:233px; top:768px; width:100px;"><b>Ankle function</b> to a delayed weight-bearing strategy</p>
  <div class="abs placeholder-art scale-art" role="img" aria-label="Illustration of weighing scales and a tape measure"></div>
  <p class="abs key-caption" style="left:498px; top:782px; width:90px;"><b>Weight bearing</b> cost-effective</p>
  <div class="abs findings-box">
    <ul class="tick-list">
      <li>An early weight-bearing strategy is not inferior in terms of ankle function to a delayed <b>weight-bearing strategy.</b></li>
      <li>Early weight-bearing is also likely to be <b>cost-effective.</b></li>
    </ul>
  </div>

  <div class="abs dashed-rule" style="top:953px;"></div>

  <h2 class="abs section-pill" style="left:400px; top:975px; width:440px;">ELIGIBILITY CRITERIA <small>(IF RELEVANT)</small></h2>
  <div class="abs placeholder-art patient-art" role="img" aria-label="Illustration of a patient on crutches with a leg cast"></div>
  <div class="abs age-pill"><b>Aged</b> 18 or over</div>

  <h3 class="abs criteria-heading" style="left:300px; top:1037px;">INCLUSION CRITERIA</h3>
  <ul class="abs tick-list criteria-list" style="left:300px; top:1078px; width:300px;">
    <li>Has had operative fixation for an unstable ankle fracture.</li>
    <li>Surgery was performed within 14 days of the injury.</li>
    <li>The treating surgeon considers that the participant might benefit from early weight-bearing.</li>
    <li>Able and willing to give informed consent</li>
  </ul>

  <div class="abs placeholder-art foot-art" role="img" aria-label="Illustration of an ankle examined under a magnifying glass"></div>

  <h3 class="abs criteria-heading" style="left:845px; top:1037px;">EXCLUSION CRITERIA</h3>
  <ul class="abs tick-list criteria-list" style="left:845px; top:1078px; width:340px;">
    <li>A lack of protective sensation (e.g. peripheral neuropathy).</li>
    <li>Inability to adhere to trial procedures.</li>
    <li>Bilateral operatively treated ankle fractures.</li>
    <li>Already in a trial for ankle fracture.</li>
    <li>Patient has received a hindfoot nail to treat index fracture.</li>
  </ul>

  <div class="abs dashed-rule" style="top:1308px;"></div>

  <h2 class="abs section-pill" style="left:395px; top:1326px; width:452px;">STUDY DETAILS <small>(IF RELEVANT)</small></h2>

  <div class="abs detail-col" style="left:60px; width:222px;">
    <div class="detail-icon" role="img" aria-label="Icon of a group of people" style="background:linear-gradient(160deg,#5a8fd6,#f08a3a);"></div>
    <div class="detail-small">Randomised</div>
    <div class="detail-big">CONTROLLED TRIAL</div>
  </div>
  <div class="abs detail-divider" style="left:320px;"></div>
  <div class="abs detail-col" style="left:330px; width:260px;">
    <div class="detail-icon" role="img" aria-label="Icon of a group of adults" style="background:linear-gradient(160deg,#f2c14e,#7a5b3a);"></div>
    <div class="detail-big">561 ADULTS</div>
    <div class="detail-small">Recruited from 23 PHS<br>hospitals in the UK</div>
  </div>
  <div class="abs detail-divider" style="left:598px;"></div>
  <div class="abs detail-col" style="left:608px; width:280px;">
    <div class="detail-icon" role="img" aria-label="Icon of a telescope on books" style="background:linear-gradient(160deg,#3a8fd6,#d63a3a);"></div>
    <div class="detail-big">A NON-INFERIORITY</div>
    <div class="detail-small">Study</div>
  </div>
  <div class="abs detail-divider" style="left:895px;"></div>
  <div class="abs detail-col" style="left:905px; width:300px;">
    <div class="detail-icon" role="img" aria-label="Icon of a painful foot" style="background:linear-gradient(160deg,#f6d3c2,#d33a3a);"></div>
    <div class="detail-small">Ankle function, quality of<br>life an complications<br>were collected at</div>
    <div class="detail-accent">6 WEEKS, 4 MONTHS &amp; 12 MONTHS AFTER</div>
  </div>

  <div class="abs dashed-rule" style="top:1566px;"></div>

  <h2 class="abs section-pill" style="left:60px; top:1588px; width:346px; height:34px; line-height:34px; font-size:23px; text-align:left; padding-left:22px;">CONTACT INFORMATION</h2>
  <h2 class="abs section-pill" style="left:693px; top:1588px; width:177px; height:34px; line-height:34px; font-size:23px;">FUNDER</h2>

  <div class="abs contact-email">
    <svg width="24" height="18" viewBox="0 0 24 18" aria-hidden="true">
      <rect x="1" y="1" width="22" height="16" fill="none" stroke="#f07d1a" stroke-width="2"/>
      <path d="M1 1 L12 10 L23 1" fill="none" stroke="#f07d1a" stroke-width="2"/>
    </svg>
    <span>recoverystudies@marlowvale.ac.uk</span>
  </div>
  <div class="abs partner-row">
    <span class="partner"><span class="partner-square" style="background:#c0392b;"></span>KESTREL INJURY AND ACUTE CARE</span>
    <span class="partner"><span class="partner-square" style="background:#f0a21a;"></span>PTQ</span>
  </div>

  <p class="abs funder-copy">National Council for Clinical Research, Research for Patient Benefit programme (RP-GR-0418-31057), supported by the NCCR Marlow Vale Biomedical Research Centre</p>

  <div class="abs footer-bar"></div>
</main>
</body>
</html>
```